TrellanVita Website - Biologics storage and handling

I would like a beginning design on a website for TrellanVita:

A Boston-based company dedicated to sourcing, storing, and supplying biologic materials of all kinds to the life sciences and scientific markets. From starting reagents, to basic and intermediate materials, to final synthesized and engineered products, we provide value throughout the biologics supply chain. TrellanVita provides backup, overflow, emergency, and stocking storage solutions to companies on a temporary or permanent basis. Life sciences companies can take advantage of the fact that the company is located in the middle of the Boston/Cambridge biotechnology corridor in order to have quick and efficient access to their cold chain materials. Out of state companies can leverage TrellanVita’s location for efficient distribution of materials to partner and client organizations. We also provide other value added services to organizations that do not have the local manpower, such as sourcing, supply, and distribution of materials.

The design should be mostly a white background with clean, linear, geometric colors added in according to the blue and orange color scheme represented in the corporate logo attached.

The website needs to communicate reliable service and provide the concept of a company dedicated to handling and providing client biological samples in a secure and efficient manner.

Some local competitors are:
1. Korbel BioWorks: www.korbelbw.example
2. LabVault: www.labvault-store.example

From a design perspective, I like the Halvenor Thera website:

www.halvenorthera.example

Target Market(s)

Life sciences companies and other organizations

Industry/Entity Type

Biotechnology

Coding

Coded - Design and coding required

Number of Pages Required

5+ page

Font styles to use
Sans Serif

Colors
3176b5
0455a3
f37122

Requirements
Must have
• Tabs for pages:
About - Company information.
Platform - Inventory and sample management cloud platform; temperature profiling, logging, and reporting.
Services - Refrigeration and freezing services for biological samples, logistics services, sourcing services, courier services.
Updates - News, events, blog.
Login portal - Entry point for getting into platform. Maybe some freemium content here.
Nice to have
• Please be creative about website page sections, vibrant colors according to my established color scheme, and clean, linear, geometric shapes. I would like a white background with nice colors, clean lines and borders, and a very contemporary look. I want o
Should not have
• This is not a Business to Consumer business. This is a Business to Business enterprise. There should not be consumer oriented language. It is more about service and relationship management.

```html
<!DOCTYPE html>
<html lang="en">
<head>
<meta charset="utf-8">
<title>TrellanVita — Biological Materials</title>
<link rel="stylesheet" href="https://fonts.googleapis.com/css2?family=Montserrat:wght@300;400;500;600;700&family=Open+Sans:wght@400;600;700&display=swap">
<style>
:root{
  --orange:#d9520f;
  --orange-bright:#f76a1e;
  --orange-btn:#f37122;
  --blue:#0d559f;
  --teal:#1f5d6e;
  --ink:#1d2731;
  --text:#5b5b5b;
  --muted:#8c8c8c;
  --mist:#f4f3f4;
  --footer:#25272f;
  --footer-dark:#1b1c21;
  --white:#ffffff;
}
*{margin:0;padding:0;box-sizing:border-box}
html,body{width:1200px;height:3077px;overflow:hidden}
body{position:relative;font-family:"Montserrat",sans-serif;color:var(--text);background:var(--white)}
.abs{position:absolute}

/* hero */
.hero{position:absolute;left:0;top:0;width:1200px;height:634px;overflow:hidden}
.hero svg{position:absolute;left:0;top:0}
.brand{position:absolute;left:80px;top:72px;display:flex;align-items:center;gap:12px;color:var(--white);font-weight:600;font-size:27px;letter-spacing:.5px}
.brand-mark{width:22px;height:22px;border:2px solid var(--white)}
.nav{position:absolute;left:430px;top:48px;display:flex;gap:20px;font-size:10.5px;font-weight:500;color:var(--white)}
.hero-title{position:absolute;left:200px;top:212px;font-size:62px;line-height:58px;font-weight:600;color:var(--white);letter-spacing:-.5px}
.hero-copy{position:absolute;left:201px;top:359px;width:360px;font-size:16px;line-height:19px;color:var(--white)}
.btn-light{position:absolute;left:201px;top:456px;width:160px;height:36px;background:var(--white);color:var(--orange);font-size:11.5px;font-weight:500;display:flex;align-items:center;justify-content:center}

/* section heads */
.sec-title{position:absolute;left:0;width:1200px;text-align:center;font-weight:600;color:var(--ink);font-size:31px;letter-spacing:.3px}
.sec-sub{position:absolute;left:495px;width:212px;display:flex;align-items:center;gap:8px;font-size:9px;font-weight:600;color:var(--teal)}
.sec-sub::before,.sec-sub::after{content:"";flex:1;height:1px;background:var(--teal);opacity:.6}

/* services */
.services{position:absolute;left:0;top:634px;width:1200px;height:570px;background:var(--mist)}
.tabs{position:absolute;left:224px;top:821px;width:738px;height:46px;background:var(--blue);display:flex;gap:36px;padding-left:46px;align-items:center;font-size:12px;color:var(--white)}
.tab-active{position:relative}
.tab-active::after{content:"";position:absolute;left:0;right:0;bottom:-7px;height:2px;background:var(--white)}
.service-photo{position:absolute;left:224px;top:895px;width:347px;height:251px;background:linear-gradient(120deg,#e9f2f7 0%,#b6d3e4 45%,#3a8fb8 80%,#1d6f98 100%)}
.service-h{position:absolute;left:617px;top:888px;font-size:25px;font-weight:600;color:var(--ink)}
.service-p{position:absolute;left:617px;width:346px;font-size:10.5px;line-height:15px;color:#666}
.btn-orange{position:absolute;background:var(--orange-btn);color:var(--white);font-size:11px;font-weight:600;display:flex;align-items:center;justify-content:center}

/* storage */
.storage-title{position:absolute;left:0;top:1262px;width:1200px;text-align:center;font-size:24.5px;line-height:30px;font-weight:500;color:var(--teal)}
.net{position:absolute;top:1300px;width:220px;height:360px;background:radial-gradient(ellipse at center,rgba(150,170,180,.12),rgba(255,255,255,0) 70%)}
.storage-card{position:absolute;left:240px;top:1371px;width:715px;height:334px;background:var(--white);box-shadow:0 2px 10px rgba(0,0,0,.12);padding:52px 34px 0;text-align:center;font-size:11.6px;line-height:18.7px;color:#555}
.storage-card p{margin-bottom:18.7px}

/* why */
.why{position:absolute;left:0;top:1791px;width:1200px;height:296px;background:linear-gradient(100deg,#ff5a1a 0%,#fb6424 50%,#ff6e30 100%);overflow:hidden}
.why-title{position:absolute;left:0;top:35px;width:1200px;text-align:center;color:var(--white);font-size:23px;font-weight:500}
.why-item{position:absolute;top:160px;display:flex;gap:17px;align-items:center;color:#ffe2d4;font-size:19.5px;font-weight:300;line-height:25px}

/* news */
.card{position:absolute;top:2259px;width:231px;height:427px;background:var(--white);border:1px solid #ececec;font-family:"Open Sans",sans-serif}
.card-img{width:229px;height:231px}
.badge{position:absolute;left:18px;top:18px;background:var(--orange-btn);color:var(--white);font-size:7.5px;font-weight:700;padding:5px 8px;font-family:"Montserrat",sans-serif}
.meta{position:absolute;left:19px;top:251px;font-size:8.5px;color:#888}
.card-h{position:absolute;left:19px;top:278px;width:195px;font-size:14px;line-height:19px;font-weight:700;color:#222}
.card-p{position:absolute;left:19px;top:324px;width:190px;font-size:10.5px;line-height:16px;color:#999}
.more{position:absolute;left:19px;top:400px;font-size:10px;font-weight:600;color:#222}

/* footer */
.footer{position:absolute;left:0;top:2755px;width:1200px;height:281px;background:var(--footer);color:#d6d6d6;font-size:10.5px}
.foot-brand{position:absolute;left:228px;top:38px;font-size:24px;font-weight:600;color:var(--orange-btn)}
.foot-h{position:absolute;top:37px;font-size:11.5px;font-weight:700;color:var(--white)}
.foot-list{position:absolute;left:419px;top:72px;list-style:none;font-size:9.5px;line-height:25.5px}
.social{position:absolute;top:2930px;width:28px;height:28px;border-radius:50%;background:#3a3d46}
.copyright{position:absolute;left:0;top:3036px;width:1200px;height:41px;background:var(--footer-dark);color:#cfcfcf;font-size:8.5px;display:flex;align-items:center;justify-content:center;gap:4px}
</style>
</head>
<body>

<header class="hero">
  <svg width="1200" height="634" viewBox="0 0 1200 634">
    <rect role="img" aria-label="Laboratory shelves with glass bottles and reagent flasks" x="0" y="0" width="1200" height="634" fill="url(#lab)"/>
    <defs>
      <linearGradient id="lab" x1="0" y1="0" x2="1" y2="1">
        <stop offset="0" stop-color="#c9ccd0"/>
        <stop offset=".5" stop-color="#9aa1a8"/>
        <stop offset=".75" stop-color="#8c6a6e"/>
        <stop offset="1" stop-color="#b7bcc2"/>
      </linearGradient>
    </defs>
    <path d="M0 0 H640 C560 120 540 250 570 360 C592 450 612 560 652 634 H0 Z" fill="var(--orange)"/>
  </svg>
  <div class="brand"><span class="brand-mark"></span>TrellanVita</div>
  <nav class="nav"><span>Home</span><span>About</span><span>Biological Storage</span><span>Materials Supply</span><span>Cold Chain Logistics</span><span>Why TrellanVita</span><span>Contact</span></nav>
  <h1 class="hero-title">Biological<br>Materials</h1>
  <p class="hero-copy">TrellanVita is dedicated to sourcing, storing, and supplying biologic materials of all kinds to the life sciences and scientific markets</p>
  <a class="btn-light">KNOW MORE</a>
</header>

<section class="services"></section>
<h2 class="sec-title" style="top:700px">OUR SERVICES</h2>
<div class="sec-sub" style="top:748px">WORK AREA</div>
<div class="tabs"><span class="tab-active">Backup</span><span>Overflow</span><span>Emergency</span><span>Stocking Storage Solutions</span><span>ManPower</span><span>Resource</span></div>
<div class="service-photo" role="img" aria-label="Scientist in blue gloves pipetting into a flask"></div>
<h3 class="service-h">Backup Process</h3>
<p class="service-p" style="top:934px">Excepteur sint occaecat cupidatat non proident sunt in culpa qui officia desunt mollit anim id est laborum. sed ut per spiciatis unde omnis natus error vitae inventore veritatis quasi architebeatae vitae dicta sunt explicabo nemo enim ipsam voluptatem quia voluptassit.aspernatur aut odit aut fugit sed quia eos consequntur magni dolores eos qui ratione</p>
<p class="service-p" style="top:1039px">Sequi nesciunt neque porro qusquam est qui dolore ipsum quia dolor sit amet consecteturadipisc velit sed quia non numquam eius modi.</p>
<a class="btn-orange" style="left:614px;top:1112px;width:102px;height:34px">READ MORE</a>

<div class="net" style="left:0" role="img" aria-label="Faint network of connected dots"></div>
<div class="net" style="left:980px" role="img" aria-label="Faint network of connected dots"></div>
<h2 class="storage-title">Biological &amp; Pharmaceutical Storage Facilities<br>Services</h2>
<div class="storage-card">
  <p>TrellanVita offers dedicated Pharmaceutical, Biological, and Consumer Products Sample Management Services in its fully cGMP compliant state of the art facilities.&nbsp; LabVault stores over 30,000,000 of our clients most precious and valuable samples in over 300 freezers and walk in rooms. Our state-of-the-art facilities are located throughout the U.S. We are currently expanding, and service the ever-increasing global market. We offer everything from cold chain delivery to cold storage in our Boston/Cambridge biotechnology corridor.</p>
  <p>Whether clients are storing 3 or 3,000,000 samples LabVault offers the same customer focused service, which allows clients unprecedented access and control of samples. With an integrated cold chain logistics fleet, LabVault is able to offer complete chain of custody and audit trail for each and every sample.</p>
  <p>LabVault is quickly establishing itself as a global leader in pharmaceutical and biological sample management and is dedicated to the specific needs of each individual customer/partner.</p>
</div>

<section class="why">
  <svg class="abs" style="left:0;top:0" width="1200" height="296">
    <polygon points="0,0 300,0 180,296 0,296" fill="#ffffff" opacity=".04"/>
    <polygon points="300,0 700,0 560,296 180,296" fill="#000000" opacity=".025"/>
    <polygon points="900,0 1200,0 1200,296 780,296" fill="#ffffff" opacity=".05"/>
  </svg>
  <h2 class="why-title">Why Chose Us?</h2>
  <div class="why-item" style="left:208px"><svg width="20" height="20" viewBox="0 0 20 20"><circle cx="10" cy="10" r="9" fill="none" stroke="#ffd9c6" stroke-width="1"/><path d="M6 10.3l2.7 2.6L14 7.5" fill="none" stroke="#ffd9c6" stroke-width="1.2"/></svg><span>Trusted<br>Competent</span></div>
  <div class="why-item" style="left:402px;top:163px"><svg width="20" height="20" viewBox="0 0 20 20"><circle cx="10" cy="10" r="9" fill="none" stroke="#ffd9c6" stroke-width="1"/><path d="M6 10.3l2.7 2.6L14 7.5" fill="none" stroke="#ffd9c6" stroke-width="1.2"/></svg><span>Dedication<br>Customizable</span></div>
  <div class="why-item" style="left:614px;top:163px"><svg width="20" height="20" viewBox="0 0 20 20"><circle cx="10" cy="10" r="9" fill="none" stroke="#ffd9c6" stroke-width="1"/><path d="M6 10.3l2.7 2.6L14 7.5" fill="none" stroke="#ffd9c6" stroke-width="1.2"/></svg><span>Clear Price<br>Compliant</span></div>
  <div class="why-item" style="left:801px;top:163px"><svg width="20" height="20" viewBox="0 0 20 20"><circle cx="10" cy="10" r="9" fill="none" stroke="#ffd9c6" stroke-width="1"/><path d="M6 10.3l2.7 2.6L14 7.5" fill="none" stroke="#ffd9c6" stroke-width="1.2"/></svg><span>Infrastructure<br>Man Power</span></div>
</section>

<h2 class="sec-title" style="top:2158px">LATEST NEWS</h2>
<div class="sec-sub" style="top:2206px">BLOG AREA</div>

<article class="card" style="left:233px">
  <div class="card-img" role="img" aria-label="Person working on a laptop" style="background:linear-gradient(160deg,#ddd8d2,#b7b0a8 60%,#8e8a86)"></div>
  <span class="badge">LATEST NEWS 1</span>
  <div class="meta">By Admin &nbsp;|&nbsp; Mar 21, 2019</div>
  <h3 class="card-h">Lacinia eget consecte sed convallis.</h3>
  <p class="card-p">Quasi architebeatae vitae dicta sunt explicabo nemo enim ipsam volupatem quia voluptassit asper natur aut ...</p>
  <div class="more">Continue Reading &nbsp;⟶</div>
</article>
<article class="card" style="left:482px">
  <div class="card-img" role="img" aria-label="Gloved hand placing a sample dish under a microscope" style="background:linear-gradient(160deg,#e2e4e6,#a9afb4 55%,#3b3f44)"></div>
  <span class="badge">LATEST NEWS 1</span>
  <div class="meta">By Admin &nbsp;|&nbsp; Mar 21, 2019</div>
  <h3 class="card-h">Haematopoietic stem cell transplant.</h3>
  <p class="card-p">Quasi architebeatae vitae dicta sunt explicabo nemo enim ipsam volupatem quia voluptassit asper natur aut ...</p>
  <div class="more">Continue Reading &nbsp;⟶</div>
</article>
<article class="card" style="left:732px">
  <div class="card-img" role="img" aria-label="Gloved hand placing a sample dish under a microscope" style="background:linear-gradient(160deg,#e2e4e6,#a9afb4 55%,#3b3f44)"></div>
  <span class="badge">LATEST NEWS 1</span>
  <div class="meta">By Admin &nbsp;|&nbsp; Mar 21, 2019</div>
  <h3 class="card-h">Excepteur sint occaecat cupidatat.</h3>
  <p class="card-p">Quasi architebeatae vitae dicta sunt explicabo nemo enim ipsam volupatem quia voluptassit asper natur aut ...</p>
  <div class="more">Continue Reading &nbsp;⟶</div>
</article>

<footer class="footer">
  <div class="foot-brand">TrellanVita</div>
  <p class="abs" style="left:230px;top:78px;width:172px;line-height:16.5px">Lorem ipsum dolor amet constetur adipisicing elit sed eiusm tempor dunt labore dolore magna aliqua enim ad minim veniam.</p>
  <div class="foot-h" style="left:419px">Quick Link</div>
  <ul class="foot-list"><li>› Home</li><li>› Research</li><li>› Publications</li><li>› Our Events</li><li>› Future Team</li></ul>
  <div class="foot-h" style="left:609px">Latest Posts</div>
  <p class="abs" style="left:609px;top:74px;width:160px;line-height:16px">Immunology: T-cell tweaks to target tumours.</p>
  <p class="abs" style="left:609px;top:113px">▦&nbsp; Mar 28, 2019</p>
  <div class="abs" style="left:609px;top:135px;width:170px;height:1px;background:#55585f"></div>
  <p class="abs" style="left:609px;top:150px;width:160px;line-height:16px">Haematopoietic stem cell transplant.</p>
  <p class="abs" style="left:609px;top:189px">▦&nbsp; Mar 28, 2019</p>
  <div class="foot-h" style="left:799px">NewsLetter</div>
  <p class="abs" style="left:799px;top:74px;width:160px;line-height:16px">Lorem ipsum dolor sit amet, consect etur adipisicing.</p>
  <div class="abs" style="left:799px;top:114px;width:169px;height:30px;background:#3a3d45;color:#9a9a9a;font-size:9px;padding:10px 13px">Enter your email</div>
  <a class="btn-orange" style="left:798px;top:158px;width:107px;height:33px;font-size:10px">SUBSCRIBE</a>
</footer>
<div class="social" style="left:231px"></div>
<div class="social" style="left:268px"></div>
<div class="social" style="left:305px"></div>
<div class="social" style="left:342px"></div>
<div class="copyright">© 2020, ALL RIGHTS RESERVED, <span style="color:var(--orange-btn)">TRELLANVITA</span></div>

</body>
</html>
```